Web Design Project for Communications Agency

The design I need (PSD file) is for an agency offering specialised PR and communications services for customers in the healthcare sector.

OBJECTIVES OF THE WEBSITE:
1. To promote the agency's communication services
2. To position Solène Verbruggen as an industry leader, an expert in healthcare PR and communications by highlighting blogposts and social media.

WHAT I NEED:
1st, I need the design for the Home Page ONLY.
Once approved, I will need the other pages designed as well. (Here is prototype that we've already developed for the Website that will guide you in the design:
http://qoravenlab.com/solenverbruggen/)

VISUAL INSPIRATION
We want to give this Website a "Flat Design" look. Here are some websites for inspiration :
- http://lumbrafolk.com/#!/process
- http://www.quillmarsh.co/
- http://dorvellink.com/

Also, reuse images found on the company's current Website :
http://www.solenverbruggen.com/fr/index.html

HOMEPAGE MAIN ELEMENTS:
1. Main menu : 6 sections
Accueil | Agence | Services | Approche | Publications | Contact

2. Main Call To Action (big dark rectangle in prototype):
Can be slider or just an information bloc.

3. Publications récentes :
The 4 latest blog posts must be features on the homepage (will be linked with the "Publications" section)

4. Dynamic Footer :
Contains a Piperly feed and a Subscribe to our Newsletter feature (revecez nos publications)

OTHER PAGES (to design once Homepage is approved)
- Agence (about us)
- Services (our team)
- Approche (our approach)
- Publications (blog articles)
- Contact (Contact us)

• Please refer to prototype :
http://qoravenlab.com/solenverbruggen/
Must have ALL features present in prototype.

Also, must reuse this picture in the design : http://solenverbruggen.com/static/images/home-big-box.jpg

Finally, you will find attached the company logo.

```html
<!DOCTYPE html>
<html lang="fr">
<head>
<meta charset="utf-8">
<title>Solène Verbruggen — Accueil</title>
<link rel="stylesheet" href="https://fonts.googleapis.com/css2?family=Anton&family=Arimo:wght@400;700&family=Oswald:wght@400;500&family=Ubuntu:wght@400;500;700&display=swap">
<style>
:root{
  --dark:#3d3d3d;
  --red:#e63c43;
  --wine:#a3363b;
  --wine-deep:#973136;
  --card:#f1f0f0;
  --card-light:#f7f6f6;
  --grey-title:#7b7b7b;
  --text:#555;
  --white:#fff;
  --field:#f1f1f1;
  --follow:#1fa3e4;
  --icon:#b8474c;
}
*{box-sizing:border-box;margin:0;padding:0}
html,body{width:714px;height:1200px;overflow:hidden}
body{position:relative;background:var(--white);font-family:"Arimo",Arial,sans-serif;color:var(--text)}

.site-header{position:absolute;left:0;top:0;width:714px;height:55px;background:var(--dark)}
.brand{position:absolute;left:37px;top:9px;width:80px;font-family:"Oswald",sans-serif;font-weight:400;font-size:15px;line-height:17px;color:var(--white)}
.main-nav{position:absolute;left:214px;top:18px;display:flex;gap:17px;font-family:"Ubuntu",sans-serif;font-size:11px;color:var(--white)}
.main-nav .active{color:var(--red)}
.nav-pointer{position:absolute;left:224px;top:45px;width:0;height:0;border-left:9px solid transparent;border-right:9px solid transparent;border-bottom:10px solid var(--wine)}

.hero{position:absolute;left:0;top:55px;width:714px;height:348px;background:linear-gradient(135deg,var(--wine),var(--wine-deep))}
.lang{position:absolute;right:41px;top:5px;font-size:10px;color:var(--white)}
.hero-badge{position:absolute;left:270px;top:36px;width:171px;height:171px;border-radius:50%;background:var(--white);display:flex;align-items:center;justify-content:center;text-align:center;font-family:"Oswald",sans-serif;font-weight:400;font-size:27px;line-height:31px;color:var(--red)}
.tagline{position:absolute;left:180px;top:224px;width:354px;text-align:center;font-size:14.5px;line-height:22px;color:var(--white)}
.btn{display:inline-flex;align-items:center;gap:5px;background:var(--red);color:var(--white);font-family:"Ubuntu",sans-serif;box-shadow:1px 1px 0 rgba(0,0,0,.25)}
.btn svg{flex:none}
.hero-cta{position:absolute;left:301px;top:279px;height:29px;padding:0 11px;font-size:13px}
.social{position:absolute;left:601px;top:318px;display:flex;gap:3px}
.social span{width:22px;height:22px;border-radius:50%;background:var(--dark);display:flex;align-items:center;justify-content:center}
.hero-rule{position:absolute;left:0;top:403px;width:714px;height:3px;background:var(--red)}

.section-title{position:absolute;left:33px;top:426px;font-family:"Anton",sans-serif;font-size:22px;color:var(--red);font-weight:400}
.band{position:absolute;left:0;top:698px;width:714px;height:268px;background:linear-gradient(135deg,var(--wine),var(--wine-deep))}

.post{position:absolute;width:318px;height:225px;background:var(--card);padding:10px 8px 0 8px}
.band-row .post{background:var(--card-light)}
.post-photo{float:left;width:130px;height:115px;margin:0 12px 0 1px}
.post-title{font-family:"Anton",sans-serif;font-weight:400;font-size:15.5px;line-height:19px;color:var(--grey-title);margin-top:-2px}
.band-row .post-title{color:var(--red)}
.post-date{display:flex;justify-content:flex-end;align-items:center;gap:4px;font-size:9.5px;color:var(--red);padding:3px 8px 3px 0;border-bottom:1px solid #e7b8ba;margin-right:8px;margin-bottom:4px}
.post-body{font-size:8.6px;line-height:10.8px;text-align:justify;hyphens:auto;-webkit-hyphens:auto;color:var(--text);margin-right:8px}
.post-more{position:absolute;right:12px;bottom:18px;height:21px;padding:0 7px;font-size:9.5px}

.back-top{position:absolute;left:333px;top:979px;width:51px;height:51px;border-radius:50%;background:var(--red);color:var(--white);font-size:8px;line-height:10px;text-align:center;padding-top:12px}

.site-footer{position:absolute;left:0;top:1034px;width:714px;height:166px;background:var(--dark);color:var(--white)}
.feed-name{position:absolute;left:89px;top:10px;font-family:"Ubuntu",sans-serif;font-weight:700;font-size:22px;letter-spacing:.5px;color:var(--white);display:flex;align-items:center;gap:6px}
.feed-name span{width:14px;height:14px;border-radius:50%;background:var(--follow)}
.tweets{position:absolute;left:89px;top:50px;width:192px;font-family:"Ubuntu",sans-serif;font-size:9px;line-height:9.3px}
.tweets p{margin-bottom:9px}
.tweets .handle{color:var(--red)}
.follow{position:absolute;left:89px;top:132px;width:103px;height:17px;background:var(--follow);display:flex;align-items:center;gap:5px;padding-left:5px;font-size:7px;font-weight:700}
.follow span{width:9px;height:9px;background:var(--white)}
.signup{position:absolute;left:429px;top:13px;width:186px}
.signup h2{font-family:"Anton",sans-serif;font-weight:400;font-size:15.5px;color:var(--white);margin-bottom:7px}
.field{height:23px;background:var(--field);color:#aaa;font-size:13px;padding:3px 7px;margin-bottom:9px}
.subscribe{width:184px;height:30px;justify-content:center;font-size:12.5px;margin-top:1px}
.copyright{margin-top:12px;font-family:"Ubuntu",sans-serif;font-size:8.5px;color:#aaa;text-align:right;padding-right:1px}
</style>
</head>
<body>

<header class="site-header">
  <div class="brand">Solène Verbruggen</div>
  <nav class="main-nav">
    <span class="active">Accueil</span><span>Services</span><span>Publications</span><span>Agence</span><span>Approche</span><span>Contact</span>
  </nav>
  <div class="nav-pointer"></div>
</header>

<section class="hero">
  <div class="lang">English</div>
  <div class="hero-badge">Solène<br>Verbruggen</div>
  <p class="tagline">Cabinet-conseil en communications et affaires publiques spécialisé dans le secteur de la santé.</p>
  <a class="btn hero-cta">En Savoir plus
    <svg width="11" height="11" viewBox="0 0 12 12"><circle cx="6" cy="6" r="5" fill="none" stroke="#fff" stroke-width="1.2"/><path d="M6 3.3v5.4M3.3 6h5.4" stroke="#fff" stroke-width="1.2"/></svg>
  </a>
  <div class="social">
    <span><svg width="12" height="12" viewBox="0 0 12 12"><circle cx="6" cy="4" r="2.3" fill="#b8474c"/><path d="M1.5 11.5c0-3 2-4.5 4.5-4.5s4.5 1.5 4.5 4.5z" fill="#b8474c"/></svg></span>
    <span><svg width="12" height="12" viewBox="0 0 12 12"><path d="M1.5 2h9v6h-5l-2.5 2.5V8h-1.5z" fill="#b8474c"/></svg></span>
    <span><svg width="12" height="12" viewBox="0 0 12 12"><rect x="1.5" y="3" width="9" height="6.5" fill="none" stroke="#b8474c" stroke-width="1.2"/><path d="M1.5 3l4.5 3.5L10.5 3" fill="none" stroke="#b8474c" stroke-width="1.2"/></svg></span>
  </div>
</section>
<div class="hero-rule"></div>

<h1 class="section-title">Publication récentes</h1>

<div class="first-row">
  <article class="post" style="left:32px;top:463px">
    <div class="post-photo" role="img" aria-label="Photo d'une présentation en salle de réunion" style="background:linear-gradient(135deg,#6e6058,#b8a27a 55%,#3b302c)"></div>
    <h3 class="post-title">Titre de la publication</h3>
    <div class="post-date"><svg width="8" height="8" viewBox="0 0 10 10"><circle cx="5" cy="5" r="4" fill="none" stroke="#e63c43"/><path d="M5 2.5V5l-1.5 1.5" stroke="#e63c43" fill="none"/></svg>23 juillet 2013</div>
    <p class="post-body">Lorem ipsum dolor sit amet, consectetur adipisicing elit, sed do eiusmod tempor incididunt ut labore et dolore magna aliqua. Ut enim ad minim veniam, quis nostrud exercitation ullamco laboris nisi ut aliquip ex ea commodo consequat. Duis aute irure dolor in reprehenderit in voluptate velit esse Duis aute irure dolor in reprehenderit in voluptate velit esse cillum dolore eu fugiat nulla pariatur. Excepteur sint occaecat cupidatat non proident, sunt in culpa qui officia deserunt mollit anim id est laborum.</p>
    <a class="btn post-more">Article complet <svg width="9" height="9" viewBox="0 0 12 12"><circle cx="6" cy="6" r="5" fill="none" stroke="#fff" stroke-width="1.2"/><path d="M6 3.3v5.4M3.3 6h5.4" stroke="#fff" stroke-width="1.2"/></svg></a>
  </article>
  <article class="post" style="left:364px;top:463px">
    <div class="post-photo" role="img" aria-label="Photo d'un patient âgé souriant avec un soignant" style="background:linear-gradient(135deg,#e9e6e2,#c9b3a3 55%,#8f7d72)"></div>
    <h3 class="post-title">Titre de la publication</h3>
    <div class="post-date"><svg width="8" height="8" viewBox="0 0 10 10"><circle cx="5" cy="5" r="4" fill="none" stroke="#e63c43"/><path d="M5 2.5V5l-1.5 1.5" stroke="#e63c43" fill="none"/></svg>23 juillet 2013</div>
    <p class="post-body">Lorem ipsum dolor sit amet, consectetur adipisicing elit, sed do eiusmod tempor incididunt ut labore et dolore magna aliqua. Ut enim ad minim veniam, quis nostrud exercitation ullamco laboris nisi ut aliquip ex ea commodo consequat. Duis aute irure dolor in reprehenderit in voluptate velit esse Duis aute irure dolor in reprehenderit in voluptate velit esse cillum dolore eu fugiat nulla pariatur. Excepteur sint occaecat cupidatat non proident, sunt in culpa qui officia deserunt mollit anim id est laborum.</p>
    <a class="btn post-more">Article complet <svg width="9" height="9" viewBox="0 0 12 12"><circle cx="6" cy="6" r="5" fill="none" stroke="#fff" stroke-width="1.2"/><path d="M6 3.3v5.4M3.3 6h5.4" stroke="#fff" stroke-width="1.2"/></svg></a>
  </article>
</div>

<section class="band band-row">
  <article class="post" style="left:32px;top:22px">
    <div class="post-photo" role="img" aria-label="Photo d'une personne avec un porte-voix dans un champ" style="background:linear-gradient(180deg,#1f4fa8,#6b9be0 60%,#5f8d3a 75%,#3f6a22)"></div>
    <h3 class="post-title">Titre de la publication</h3>
    <div class="post-date"><svg width="8" height="8" viewBox="0 0 10 10"><circle cx="5" cy="5" r="4" fill="none" stroke="#e63c43"/><path d="M5 2.5V5l-1.5 1.5" stroke="#e63c43" fill="none"/></svg>23 juillet 2013</div>
    <p class="post-body">Lorem ipsum dolor sit amet, consectetur adipisicing elit, sed do eiusmod tempor incididunt ut labore et dolore magna aliqua. Ut enim ad minim veniam, quis nostrud exercitation ullamco laboris nisi ut aliquip ex ea commodo consequat. Duis aute irure dolor in reprehenderit in voluptate velit esse Duis aute irure dolor in reprehenderit in voluptate velit esse cillum dolore eu fugiat nulla pariatur. Excepteur sint occaecat cupidatat non proident, sunt in culpa qui officia deserunt mollit anim id est laborum.</p>
    <a class="btn post-more">Article complet <svg width="9" height="9" viewBox="0 0 12 12"><circle cx="6" cy="6" r="5" fill="none" stroke="#fff" stroke-width="1.2"/><path d="M6 3.3v5.4M3.3 6h5.4" stroke="#fff" stroke-width="1.2"/></svg></a>
  </article>
  <article class="post" style="left:364px;top:22px">
    <div class="post-photo" role="img" aria-label="Photo de mains jointes sur fond bleu clair" style="background:linear-gradient(135deg,#cfe3f3,#9cc4e6 50%,#e9c3ad)"></div>
    <h3 class="post-title">Titre de la publication</h3>
    <div class="post-date"><svg width="8" height="8" viewBox="0 0 10 10"><circle cx="5" cy="5" r="4" fill="none" stroke="#e63c43"/><path d="M5 2.5V5l-1.5 1.5" stroke="#e63c43" fill="none"/></svg>23 juillet 2013</div>
    <p class="post-body">Lorem ipsum dolor sit amet, consectetur adipisicing elit, sed do eiusmod tempor incididunt ut labore et dolore magna aliqua. Ut enim ad minim veniam, quis nostrud exercitation ullamco laboris nisi ut aliquip ex ea commodo consequat. Duis aute irure dolor in reprehenderit in voluptate velit esse Duis aute irure dolor in reprehenderit in voluptate velit esse cillum dolore eu fugiat nulla pariatur. Excepteur sint occaecat cupidatat non proident, sunt in culpa qui officia deserunt mollit anim id est laborum.</p>
    <a class="btn post-more">Article complet <svg width="9" height="9" viewBox="0 0 12 12"><circle cx="6" cy="6" r="5" fill="none" stroke="#fff" stroke-width="1.2"/><path d="M6 3.3v5.4M3.3 6h5.4" stroke="#fff" stroke-width="1.2"/></svg></a>
  </article>
</section>

<a class="back-top">Back to<br>Top<br>
  <svg width="6" height="9" viewBox="0 0 6 9"><path d="M3 9V1M1 3l2-2 2 2" stroke="#fff" fill="none"/></svg>
</a>

<footer class="site-footer">
  <div class="feed-name">piperly<span></span></div>
  <div class="tweets">
    <p>Velit esse eu fugiat nulla pariatur. Excepteur sint occaecat cupidatat non proident. <span class="handle">@SolenVerbruggen #EnjeuSanté</span></p>
    <p>Velit esse cillum dolore eu fugiat nulla pariatur. Excepteur sint occaecat cupidatat non proident. <span class="handle">@SolenVerbruggen #EnjeuSanté</span></p>
  </div>
  <div class="follow"><span></span>Follow us on Piperly</div>

  <form class="signup">
    <h2>Recevez nos publications</h2>
    <div class="field">Votre nom</div>
    <div class="field">Votre courriel</div>
    <a class="btn subscribe">Abonnez-vous
      <svg width="11" height="11" viewBox="0 0 12 12"><circle cx="6" cy="6" r="5" fill="none" stroke="#fff" stroke-width="1.2"/><path d="M6 3.3v5.4M3.3 6h5.4" stroke="#fff" stroke-width="1.2"/></svg>
    </a>
    <p class="copyright">(c) Solène Verbruggen. Tous droits réservés.</p>
  </form>
</footer>

</body>
</html>
```